Breast Cancer Car Donation Website Design

Please create a new one page website design.

Current site: http://www.givemyautohope.com/

The NEW website address will be RidesforPinkRibbonAid.org

Use these sites for an idea of what I am looking for. I like these sites best: drivesforheroesfund.org and autosforservicemen.org

```html
<!DOCTYPE html>
<html lang="en">
<head>
<meta charset="utf-8">
<title>Rides for Pink Ribbon Aid</title>
<link rel="stylesheet" href="https://fonts.googleapis.com/css2?family=Lato:wght@400;700;900&family=Roboto:wght@400;500;700&display=swap">
<style>
:root{
  --pink:#e0075e;
  --pink-dark:#c4004f;
  --navy:#0d2f8f;
  --navy-deep:#082a80;
  --text:#555a66;
  --heading-navy:#0f2f8c;
  --light:#f4f4f6;
  --white:#ffffff;
}
*{box-sizing:border-box;margin:0;padding:0}
html,body{width:1200px;height:2826px;overflow:hidden}
body{position:relative;font-family:'Roboto',Arial,sans-serif;color:var(--text);background:var(--white)}
.abs{position:absolute}
/* header */
.site-header{left:0;top:0;width:1200px;height:110px;background:var(--white)}
.brand{left:98px;top:14px;display:flex;align-items:center;gap:10px}
.brand-dot{width:22px;height:22px;border-radius:50%;background:var(--pink)}
.brand-name{font-family:'Lato',sans-serif;font-weight:900;font-size:20px;color:var(--pink)}
.partner-badge{left:580px;top:26px;width:106px;height:54px;background:#e9e9ef;border-radius:3px}
.main-nav{left:0;top:110px;width:1200px;height:43px;background:var(--navy)}
.main-nav ul{list-style:none;display:flex;position:absolute;left:98px;top:12px}
.main-nav li{font-family:'Lato',sans-serif;font-weight:700;font-size:15px;color:var(--white);margin-right:42px;text-transform:uppercase}
.nav-search{left:658px;top:124px}
/* hero */
.hero-photo{left:0;top:153px;width:1200px;height:467px;background:linear-gradient(180deg,#9fb9d8 0%,#3c6ea8 45%,#1e4f8c 70%,#2a5d96 100%)}
.donate-panel{left:738px;top:0;width:362px;height:620px;background:var(--pink)}
.panel-icons{left:0;top:18px;width:362px;height:70px}
.panel-banner{left:730px;top:98px;width:378px;height:38px;background:var(--white);box-shadow:0 2px 4px rgba(0,0,0,.15);font-family:'Lato',sans-serif;font-weight:700;font-size:17px;color:var(--pink);text-align:center;line-height:38px}
.panel-title{left:738px;top:164px;width:362px;text-align:center;font-family:'Lato',sans-serif;font-weight:700;font-size:20px;color:var(--white);line-height:29px}
.field{position:absolute;left:768px;width:304px;height:37px;background:var(--white);border-radius:2px;font-size:12px;color:#6c7080;padding:11px 12px}
.field.half{width:146px}
.caret{position:absolute;right:9px;top:11px;width:8px;height:14px}
.donate-btn{left:768px;top:548px;width:135px;height:36px;border-radius:18px;background:var(--navy);color:var(--white);font-family:'Roboto',sans-serif;font-weight:700;font-size:13px;text-align:center;line-height:36px;text-transform:uppercase}
/* how to donate */
.how-section{left:0;top:620px;width:1200px;height:525px;background:linear-gradient(90deg,#fff 0%,#f7f7f9 100%)}
.ghost-title{font-family:'Lato',sans-serif;font-weight:900;color:rgba(0,0,0,.06);text-transform:uppercase;white-space:nowrap}
.section-title{font-family:'Lato',sans-serif;font-weight:900;text-transform:uppercase;white-space:nowrap}
.section-title .accent{color:var(--pink)}
.section-title .base{color:var(--heading-navy)}
.video-frame{left:90px;top:723px;width:423px;height:277px;border:2px solid var(--navy);border-right:none;border-bottom:none;border-radius:12px 12px 0 12px}
.video-thumb{left:127px;top:758px;width:430px;height:280px;border-radius:8px;background:linear-gradient(160deg,#c9c7c5 0%,#8b8a8c 45%,#5c5a5c 100%);box-shadow:0 4px 14px rgba(0,0,0,.25)}
.play{left:322px;top:880px}
.step{position:absolute;left:615px;width:480px}
.step-icon{position:absolute;left:0;top:0;width:56px;height:56px;border-radius:50%}
.step-title{position:absolute;left:82px;top:0;font-family:'Roboto',sans-serif;font-weight:700;font-size:16px;color:var(--heading-navy)}
.step-text{position:absolute;left:82px;top:26px;width:410px;font-size:12.5px;line-height:21px;color:var(--text)}
.step-link{left:642px;width:2px;height:36px;border-left:2px dotted var(--pink)}
/* benefit band */
.benefit-band{left:0;top:1145px;width:1200px;height:335px;background:linear-gradient(90deg,var(--pink) 0%,#e3146a 60%,#d3065a 100%)}
.benefit{position:absolute;width:214px;text-align:center}
.benefit-circle{margin:0 auto;width:122px;height:122px;border-radius:50%;border:3px solid var(--white);padding:6px}
.benefit-circle .inner{width:104px;height:104px;border-radius:50%;background:var(--white);display:flex;align-items:center;justify-content:center}
.benefit-label{margin-top:26px;font-family:'Lato',sans-serif;font-weight:700;font-size:17px;color:var(--white)}
/* why */
.why-section{left:0;top:1480px;width:1200px;height:480px;background:var(--light)}
.reason{position:absolute;width:330px}
.reason svg{position:absolute;left:0;top:0}
.reason h4{position:absolute;left:52px;top:0;font-family:'Roboto',sans-serif;font-weight:700;font-size:13px;color:var(--heading-navy);white-space:nowrap}
.reason p{position:absolute;left:52px;top:22px;width:290px;font-size:12px;line-height:25px;color:var(--text)}
/* faq */
.faq-section{left:0;top:1960px;width:1200px;height:512px;background:#f2f2f4}
.faq-photo{left:647px;top:1960px;width:553px;height:512px;background:linear-gradient(135deg,#f3ead9 0%,#d9b9a0 35%,#c0283b 60%,#8a1020 100%)}
.faq-list{left:98px;top:2078px;width:479px;background:var(--white)}
.faq-item{position:relative;height:41px;border:1px solid #e3e3e8;margin-bottom:-1px;font-size:12.5px;color:var(--heading-navy);padding:13px 16px}
.faq-item .toggle{position:absolute;right:0;top:0;width:40px;height:39px;color:var(--pink);font-size:18px;font-weight:700;text-align:center;line-height:39px}
.faq-item.open .toggle{background:var(--pink);color:var(--white);right:-1px;top:-1px;height:41px;width:41px}
.faq-item.open{color:var(--pink)}
.faq-answer{border:1px solid #e3e3e8;border-top:none;margin-bottom:-1px;padding:18px 28px;height:104px;font-size:12.5px;line-height:23px;color:#6a6e78}
/* footer */
.site-footer{left:0;top:2472px;width:1200px;height:354px;background:linear-gradient(90deg,var(--navy-deep) 0%,#0c34a0 50%,var(--navy-deep) 100%)}
.footer-brand{left:100px;top:2600px;display:flex;align-items:center;gap:10px}
.footer-brand .brand-dot{background:var(--white)}
.footer-brand .brand-name{color:var(--white)}
.footer-heading{font-family:'Roboto',sans-serif;font-weight:700;font-size:15px;color:var(--white);text-transform:uppercase}
.footer-links{list-style:none}
.footer-links li{font-size:12.5px;color:var(--white);margin-bottom:14px}
.contact-line{position:absolute;left:876px;font-size:12px;color:var(--white);line-height:20px}
.contact-line svg{position:absolute;left:0;top:2px}
.contact-line span{display:block;margin-left:34px}
.footer-rule{left:98px;top:2772px;width:1004px;height:1px;background:rgba(255,255,255,.45)}
.copyright{left:0;top:2788px;width:1200px;text-align:center;font-size:12.5px;color:var(--white)}
</style>
</head>
<body>

<header class="site-header abs">
  <div class="brand abs"><span class="brand-dot"></span><span class="brand-name">Pink Ribbon Rides</span></div>
  <div class="partner-badge abs"></div>
</header>

<nav class="main-nav abs">
  <ul>
    <li>Donate a car or boat now</li>
    <li>About</li>
    <li>Contact</li>
    <li>FAQ</li>
  </ul>
</nav>
<svg class="nav-search abs" width="16" height="16" viewBox="0 0 16 16"><circle cx="6.5" cy="6.5" r="4.5" fill="none" stroke="#fff" stroke-width="2.2"/><line x1="10" y1="10" x2="14" y2="14" stroke="#fff" stroke-width="2.6" stroke-linecap="round"/></svg>

<div class="hero-photo abs" role="img" aria-label="Smiling woman in a headscarf standing by the sea with a red and white speedboat behind her"></div>

<section class="donate-panel abs">
  <svg class="panel-icons abs" viewBox="0 0 362 70">
    <g fill="#fff">
      <path d="M34 40 l8-12 h34 l10 12 h6 v12 h-66 v-12z M46 31 l-5 9 h14 v-9z M60 31 v9 h20 l-7-9z"/>
      <circle cx="48" cy="54" r="6" fill="#e0075e" stroke="#fff" stroke-width="3"/>
      <circle cx="84" cy="54" r="6" fill="#e0075e" stroke="#fff" stroke-width="3"/>
      <path d="M262 44 h84 l-10 12 h-66z M278 32 h30 l14 10 h-52z"/>
    </g>
  </svg>
</section>
<div class="panel-banner abs">DONATE YOUR CAR ONLINE 24/7</div>
<h1 class="panel-title abs">TAX DEDUCTION - EASY TO DO!<br>RUNNING OR NOT</h1>
<div class="field" style="top:248px">Full Name</div>
<div class="field" style="top:295px">Phone</div>
<div class="field" style="top:342px">Email</div>
<div class="field" style="top:388px">Zip Code</div>
<div class="field half" style="top:435px">Choose year<svg class="caret" viewBox="0 0 8 14"><path d="M0 5 L4 0 L8 5z M0 9 L4 14 L8 9z" fill="#333"/></svg></div>
<div class="field half" style="top:435px;left:926px">Choose Make<svg class="caret" viewBox="0 0 8 14"><path d="M0 5 L4 0 L8 5z M0 9 L4 14 L8 9z" fill="#333"/></svg></div>
<div class="field" style="top:483px">Vehicle Module</div>
<div class="donate-btn abs">Donate now</div>

<section class="how-section abs"></section>
<div class="ghost-title abs" style="left:0;top:648px;width:1200px;text-align:center;font-size:80px">How to donate</div>
<h2 class="section-title abs" style="left:615px;top:712px;font-size:36px"><span class="accent">How to</span> <span class="base">Donate</span></h2>
<div class="video-frame abs"></div>
<div class="video-thumb abs" role="img" aria-label="Rows of parked donated cars in a lot, video preview"></div>
<svg class="play abs" width="36" height="36" viewBox="0 0 36 36"><path d="M10 6 L30 18 L10 30z" fill="#fff"/></svg>

<div class="step" style="top:786px">
  <svg class="step-icon" viewBox="0 0 56 56"><circle cx="28" cy="28" r="28" fill="#e0075e"/><path d="M20 18 c-3 3 -2 9 4 15 s12 7 15 4 l-4-5 -4 2 c-2-1-5-4-6-6 l2-4z" fill="#fff"/><path d="M31 18 a8 8 0 0 1 7 7 M31 22 a4 4 0 0 1 3 3" stroke="#fff" stroke-width="2" fill="none"/></svg>
  <div class="step-title">Pick a Charity</div>
  <p class="step-text">Call Us At 1-800-555-0142 Or Fill Out The Online Form. Donating your vehicle is easy and donation is accepted nationwide.</p>
</div>
<div class="step-link abs" style="top:845px"></div>
<div class="step" style="top:877px">
  <svg class="step-icon" viewBox="0 0 56 56"><circle cx="28" cy="28" r="27" fill="#fff" stroke="#e0075e" stroke-width="2"/><path d="M15 31 h8 l3-5 h9 l4 5 h3 v5 h-27z" fill="none" stroke="#e0075e" stroke-width="2"/><circle cx="21" cy="37" r="3" fill="#e0075e"/><circle cx="36" cy="37" r="3" fill="#e0075e"/><path d="M14 30 l-3-10 h6" stroke="#e0075e" stroke-width="2" fill="none"/></svg>
  <div class="step-title">Fast &amp; Free Pick Up</div>
  <p class="step-text">Any vehicles are accepted and we will arrange to pick up your vehicle when it is most convenient for you.</p>
</div>
<div class="step-link abs" style="top:936px"></div>
<div class="step" style="top:968px">
  <svg class="step-icon" viewBox="0 0 56 56"><circle cx="28" cy="28" r="27" fill="#fff" stroke="#e0075e" stroke-width="2"/><rect x="19" y="15" width="18" height="26" rx="2" fill="none" stroke="#e0075e" stroke-width="2"/><path d="M23 22 h10 M23 27 h10 M23 32 h10" stroke="#e0075e" stroke-width="2"/></svg>
  <div class="step-title">Tax Deductible</div>
  <p class="step-text">Once the vehicle donation is complete, you will receive your tax deductable vehicle donation receipt.</p>
</div>

<section class="benefit-band abs">
  <div class="benefit" style="left:70px;top:83px">
    <div class="benefit-circle"><div class="inner"><svg width="50" height="56" viewBox="0 0 50 56"><path d="M18 4 h14 l-4 10 h-6z" fill="#e0075e"/><path d="M25 14 C5 20 2 52 25 52 C48 52 45 20 25 14z" fill="#e0075e"/><text x="25" y="44" font-family="Lato" font-weight="900" font-size="20" fill="#fff" text-anchor="middle">$</text></svg></div></div>
    <div class="benefit-label">You Have No Costs</div>
  </div>
  <div class="benefit" style="left:284px;top:83px">
    <div class="benefit-circle"><div class="inner"><svg width="60" height="52" viewBox="0 0 60 52"><path d="M8 34 h30 l4-14 h10 l6 14 v6 h-50z" fill="#e0075e"/><path d="M12 32 l-8-26 h6" stroke="#e0075e" stroke-width="4" fill="none"/><circle cx="18" cy="42" r="6" fill="#fff" stroke="#e0075e" stroke-width="4"/><circle cx="46" cy="42" r="6" fill="#fff" stroke="#e0075e" stroke-width="4"/></svg></div></div>
    <div class="benefit-label">Free Local Towing</div>
  </div>
  <div class="benefit" style="left:498px;top:83px">
    <div class="benefit-circle"><div class="inner"><svg width="44" height="56" viewBox="0 0 44 56"><path d="M4 2 h36 v52 l-6-4 -6 4 -6-4 -6 4 -6-4 -6 4z" fill="none" stroke="#e0075e" stroke-width="3.5"/><path d="M12 14 h20 M12 22 h20 M12 30 h12 M12 38 h20" stroke="#e0075e" stroke-width="3"/></svg></div></div>
    <div class="benefit-label">Income Tax Deduction</div>
  </div>
  <div class="benefit" style="left:712px;top:83px">
    <div class="benefit-circle"><div class="inner"><svg width="56" height="54" viewBox="0 0 56 54"><rect x="14" y="2" width="34" height="44" fill="none" stroke="#e0075e" stroke-width="3.5"/><path d="M22 12 h18 M28 20 h12 M28 28 h12" stroke="#e0075e" stroke-width="3"/><circle cx="18" cy="34" r="12" fill="#e0075e"/><path d="M18 27 v9 M18 39 v2" stroke="#fff" stroke-width="3"/></svg></div></div>
    <div class="benefit-label">No Paperwork</div>
  </div>
  <div class="benefit" style="left:926px;top:83px">
    <div class="benefit-circle"><div class="inner"><svg width="44" height="56" viewBox="0 0 44 56"><rect x="3" y="8" width="38" height="46" rx="3" fill="none" stroke="#e0075e" stroke-width="3.5"/><rect x="14" y="3" width="16" height="9" rx="2" fill="#e0075e"/><path d="M11 24 h22 M11 32 h22 M11 40 h14" stroke="#e0075e" stroke-width="3"/></svg></div></div>
    <div class="benefit-label">No DMV Hassles</div>
  </div>
</section>

<section class="why-section abs"></section>
<div class="ghost-title abs" style="left:0;top:1512px;width:1200px;text-align:center;font-size:78px">Why donate car</div>
<h2 class="section-title abs" style="left:0;top:1576px;width:1200px;text-align:center;font-size:34px"><span class="accent">Why donate</span> <span class="base">your car to us</span></h2>

<div class="reason" style="left:97px;top:1673px">
  <svg width="40" height="40" viewBox="0 0 40 40"><path d="M34 20 a14 14 0 1 1 -4-10" fill="none" stroke="#e0075e" stroke-width="3"/><path d="M30 4 v7 h-7" fill="none" stroke="#e0075e" stroke-width="3"/><text x="20" y="25" font-family="Roboto" font-weight="700" font-size="12" fill="#e0075e" text-anchor="middle">24</text></svg>
  <h4>IRS 501(c)3 Approved :</h4>
  <p>Free 24/7 Pickup with No DMV Hassles.</p>
</div>
<div class="reason" style="left:427px;top:1673px">
  <svg width="42" height="40" viewBox="0 0 42 40"><path d="M4 24 h20 l3-9 h7 l5 9 v6 h-35z" fill="none" stroke="#e0075e" stroke-width="3"/><path d="M7 23 l-4-16 h5" stroke="#e0075e" stroke-width="3" fill="none"/><circle cx="11" cy="32" r="4" fill="#e0075e"/><circle cx="32" cy="32" r="4" fill="#e0075e"/></svg>
  <h4>Free Local Towing :</h4>
  <p>We will pick up your car donation, running or not, when it's most convenient, at home or work.</p>
</div>
<div class="reason" style="left:798px;top:1673px">
  <svg width="40" height="40" viewBox="0 0 40 40"><path d="M8 2 h24 v36 l-4-3 -4 3 -4-3 -4 3 -4-3 -4 3z" fill="none" stroke="#e0075e" stroke-width="2.6"/><path d="M13 11 h14 M13 17 h14 M13 23 h8 M13 29 h14" stroke="#e0075e" stroke-width="2.4"/></svg>
  <h4>Income Tax Deduction :</h4>
  <p>We issue you an IRS tax receipt and get you the highest tax write-off possible.</p>
</div>
<div class="reason" style="left:97px;top:1773px">
  <svg width="40" height="40" viewBox="0 0 40 40"><rect x="5" y="5" width="28" height="32" rx="2" fill="none" stroke="#e0075e" stroke-width="2.6"/><path d="M11 14 h16 M11 20 h16 M11 26 h10" stroke="#e0075e" stroke-width="2.4"/><path d="M26 30 l10-14" stroke="#e0075e" stroke-width="3"/></svg>
  <h4>No Paperwork Hassles :</h4>
  <p>We handle everything: DMV and IRS paper-work.</p>
</div>
<div class="reason" style="left:427px;top:1773px">
  <svg width="40" height="40" viewBox="0 0 40 40"><path d="M20 4 a8 8 0 0 1 8 8 c0 6 -8 13 -8 13 s-8-7-8-13 a8 8 0 0 1 8-8z" fill="none" stroke="#e0075e" stroke-width="2.6"/><circle cx="20" cy="12" r="3" fill="#e0075e"/><path d="M4 26 l16 6 16-6 v8 l-16 5 -16-5z" fill="none" stroke="#e0075e" stroke-width="2.4"/></svg>
  <h4>Schedule a Free Pickup :</h4>
  <p>We will pick up your car donation, running or not, when it's most convenient, at home or work.</p>
</div>
<div class="reason" style="left:798px;top:1773px">
  <svg width="44" height="40" viewBox="0 0 44 40"><path d="M10 16 l4-8 h16 l5 8 h5 v8 h-34 v-8z" fill="#e0075e"/><circle cx="15" cy="25" r="3.5" fill="#fff" stroke="#e0075e" stroke-width="2"/><circle cx="31" cy="25" r="3.5" fill="#fff" stroke="#e0075e" stroke-width="2"/><path d="M2 32 h10 l8 4 h16 l6-4" fill="none" stroke="#e0075e" stroke-width="3"/></svg>
  <h4>Car donations help fund programs :</h4>
  <p>And benefit Brightpath Giving Trust an IRS 501(c)3 nonprofit organization</p>
</div>

<section class="faq-section abs"></section>
<div class="faq-photo abs" role="img" aria-label="Happy young woman leaning out of a red car window with her arm outstretched"></div>
<h2 class="section-title abs" style="left:97px;top:2016px;font-size:29px"><span class="accent">Frequently</span> <span class="base">Asked Questions</span></h2>
<div class="faq-list abs">
  <div class="faq-item">What is Perfectly Simple?<span class="toggle">+</span></div>
  <div class="faq-item open">What is Lorem Ipsum?<span class="toggle">−</span></div>
  <div class="faq-answer">Nemo enim ipsam voluptatem quia voluptas sit aspernatur aut odit aut fugit, sed quia consequuntur magni dolores eos qui ratione voluptatem at sequi nesciunt. Neque porro quisquam est, qui dolorem</div>
  <div class="faq-item">What is Itaque Earum?<span class="toggle">+</span></div>
  <div class="faq-item">What is Weakness Of Will?<span class="toggle">+</span></div>
  <div class="faq-item">What is Perfectly Simple?<span class="toggle">+</span></div>
</div>

<footer class="site-footer abs"></footer>
<div class="footer-brand abs"><span class="brand-dot"></span><span class="brand-name">Pink Ribbon Rides</span></div>
<div class="footer-heading abs" style="left:493px;top:2542px">Navigation</div>
<ul class="footer-links abs" style="left:496px;top:2588px">
  <li>Donate A Car Or Boat Now</li>
  <li>About Us</li>
  <li>Contact Us</li>
  <li>FAQ</li>
</ul>
<div class="footer-heading abs" style="left:876px;top:2542px">Contact Us</div>
<div class="contact-line" style="top:2586px">
  <svg width="14" height="18" viewBox="0 0 14 18"><path d="M7 0 a7 7 0 0 1 7 7 c0 5 -7 11 -7 11 s-7-6-7-11 a7 7 0 0 1 7-7z" fill="#fff"/><circle cx="7" cy="7" r="2.5" fill="#0d2f8f"/></svg>
  <span>123Abc Sample Street, Old City,<br>ABC State, PO 818,</span>
</div>
<div class="contact-line" style="top:2640px">
  <svg width="14" height="14" viewBox="0 0 14 14"><path d="M2 1 c-2 2 -1 6 3 9 s7 4 8 2 l-2-3 -2 1 c-1 0-3-2-4-4 l1-2z" fill="#fff"/></svg>
  <span>888 - 555 - 0199</span>
</div>
<div class="contact-line" style="top:2678px">
  <svg width="16" height="12" viewBox="0 0 16 12"><rect width="16" height="12" rx="1" fill="#fff"/><path d="M0 1 l8 6 8-6" stroke="#0d2f8f" stroke-width="1.5" fill="none"/></svg>
  <span>hello@givemyautohope.com</span>
</div>
<div class="footer-rule abs"></div>
<div class="copyright abs">© Copyright 2018 Rides for Pink Ribbon Aid. All Rights Reserved.</div>

</body>
</html>
```